Rise Past Horizon needs a new design for Business Cards

We need a business card design for our personal training business call Rise Past Horizon. We are the Sustained Weight Loss Specialists.
Our target market is overweight and obese adults who have experience the ups of loosing weight and lows of putting it back on and are looking for a sustained weight loss solution.
Our USP is: "We Smash Through The Barriers That Are Holding You Back From Sustained Weight Loss".
We would like to the design incorporate the colours of our logo, with other acceptable colours being black, white, yellow and green.
Visit our website at www.risepasthorizon.com.au for an overview of our business, and also the attached company profile.

Target Market(s)

Industry/Entity Type

Training

Colors
0092cd
eb1f27
fbed22
9bcb3c
000000
ffffff

Requirements
Must have
• Easy to read fonts
Logo (Not huge)
Call to Action (Something like, Claim your 10 Tips to Melt Body Fat, and 30 minutes PT Session VALUED AT $101)
Contact and Address details (as per footer of company profile (page 2 onwards)
List of Benefits (see company profile and website)
USP as per project overview
A picture to match the USP
Should not have
• Please do not try and copy the design of the company profile. It was slapped together.
A list of exercises

```html
<!DOCTYPE html>
<html lang="en">
<head>
<meta charset="utf-8">
<title>Rise Past Horizon – Business Cards</title>
<link href="https://fonts.googleapis.com/css2?family=Anton&family=Roboto+Condensed:wght@400;700&display=swap" rel="stylesheet">
<style>
  :root{
    --brand-blue:#4a68b0;
    --brand-blue-dark:#2f4a8c;
    --brand-red:#e0202e;
    --ink:#3a3f4a;
    --muted:#6b7280;
    --card-light:#ffffff;
    --card-grey:#d9dbe0;
    --stage:#ecebe8;
  }
  *{box-sizing:border-box;margin:0;padding:0}
  html,body{width:1200px;height:1000px;overflow:hidden;background:var(--stage)}
  .stage{position:relative;width:1200px;height:1000px}
  .card{
    position:absolute;width:520px;height:300px;border-radius:18px;overflow:hidden;
    background:linear-gradient(160deg,var(--card-light) 0%,#eef0f3 45%,var(--card-grey) 100%);
    box-shadow:0 10px 30px rgba(0,0,0,.18);
    font-family:"Roboto Condensed",Arial,sans-serif;
  }
  .card--front{left:50px;top:350px}
  .card--back{left:630px;top:350px}
  .card svg.layer{position:absolute;inset:0;width:100%;height:100%}
  .photo{position:absolute}

  /* front */
  .front-photo{right:0;top:0;width:190px;height:190px;
    background:linear-gradient(180deg,#e9e9ea 0%,#c9b2a2 35%,#2a2d35 70%,#1f232a 100%)}
  .fist-art{left:22px;top:92px;width:92px;height:96px;border-radius:14px;
    background:radial-gradient(circle at 45% 45%,#cfe6ee 0%,#7fb8c9 60%,#4a8aa3 100%)}
  .usp{position:absolute;left:124px;top:42px;width:200px;color:var(--brand-blue)}
  .usp__lead{font-family:"Anton",Impact,sans-serif;font-size:22px;line-height:1;letter-spacing:.5px;text-transform:uppercase}
  .usp__big{font-family:"Anton",Impact,sans-serif;font-size:48px;line-height:1.05;letter-spacing:1px;text-transform:uppercase;margin-top:2px}
  .usp__sub{font-weight:700;font-size:15px;line-height:1.15;margin-top:4px}
  .usp__sub em{font-style:normal;color:var(--brand-red)}
  .visit{position:absolute;left:190px;top:232px;color:#fff}
  .visit__label{font-size:14px}
  .visit__url{font-weight:700;font-size:22px;letter-spacing:.3px}

  /* back */
  .offer{position:absolute;right:18px;top:30px;width:190px;text-align:right;
    color:var(--brand-red);font-weight:700;font-size:14px;line-height:1.15}
  .offer strong{text-transform:uppercase}
  .brand{position:absolute;left:22px;top:160px;width:150px}
  .brand__dot{display:block;width:30px;height:30px;border-radius:50%;background:var(--brand-blue);margin-bottom:8px}
  .brand__name{font-size:17px;font-weight:400;color:var(--brand-red);text-transform:uppercase;letter-spacing:.5px;line-height:1}
  .brand__tag{font-size:10px;color:var(--brand-blue);margin-top:3px}
  .contacts{position:absolute;left:190px;top:160px;color:var(--ink)}
  .contact{margin-bottom:5px}
  .contact__line{font-weight:700;font-size:16px;line-height:1.05}
  .contact__name{color:var(--brand-blue);text-transform:uppercase}
  .contact__email,.contact__role{font-size:10px;color:var(--muted);line-height:1.2}
  .site{font-weight:700;font-size:14px;color:var(--brand-blue);line-height:1.2}
  .address{font-size:10px;color:var(--muted);line-height:1.2}
</style>
</head>
<body>
<div class="stage">

  <section class="card card--front" aria-label="Business card front">
    <div class="photo front-photo" role="img" aria-label="Photo of a trainer in a black t-shirt with arms crossed"></div>
    <svg class="layer" viewBox="0 0 520 300" preserveAspectRatio="none" aria-hidden="true">
      <path d="M150 300 L190 214 Q230 196 300 190 L520 174 L520 300 Z" fill="var(--brand-red)"/>
      <path d="M160 300 L198 222 Q236 204 306 198 L520 182 L520 300 Z" fill="var(--brand-blue)"/>
    </svg>
    <div class="photo fist-art" role="img" aria-label="Illustration of a clenched fist breaking through"></div>
    <div class="usp">
      <p class="usp__lead">We Smash<br>Through The</p>
      <p class="usp__big">Barriers</p>
      <p class="usp__sub">That Are Holding You Back From Sustained <em>Weight Loss</em></p>
    </div>
    <div class="visit">
      <p class="visit__label">Visit our website at</p>
      <p class="visit__url">www.risepasthorizon.com.au</p>
    </div>
  </section>

  <section class="card card--back" aria-label="Business card back">
    <svg class="layer" viewBox="0 0 520 300" preserveAspectRatio="none">
      <defs>
        <linearGradient id="waistPhoto" x1="0" y1="0" x2="1" y2="0.4">
          <stop offset="0" stop-color="#d9cfc9"/>
          <stop offset="0.35" stop-color="#c79a80"/>
          <stop offset="0.6" stop-color="#a9806c"/>
          <stop offset="0.8" stop-color="#2a3a66"/>
          <stop offset="1" stop-color="#1f2c52"/>
        </linearGradient>
      </defs>
      <path d="M118 0 Q112 96 196 128 Q280 152 520 140 L520 0 Z" fill="var(--brand-blue)" aria-hidden="true"/>
      <path d="M128 0 Q124 88 204 120 Q284 142 520 130 L520 0 Z" fill="var(--brand-red)" aria-hidden="true"/>
      <path d="M136 0 Q134 82 210 112 Q288 134 520 122 L520 0 Z" fill="url(#waistPhoto)" role="img" aria-label="Photo of a person measuring their waist with a tape measure"/>
      <path d="M490 150 L520 146 L520 300 L468 300 Q492 240 490 150 Z" fill="var(--brand-blue)" aria-hidden="true"/>
    </svg>
    <p class="offer"><strong>Claim your</strong> 10 TIPS to Melt Body Fat, and 30 minute PT Session <strong>Valued at $101</strong></p>
    <div class="brand">
      <span class="brand__dot" aria-hidden="true"></span>
      <p class="brand__name">Rise Past Horizon</p>
      <p class="brand__tag">Sustained Weight Loss Specialists</p>
    </div>
    <div class="contacts">
      <div class="contact">
        <p class="contact__line"><span class="contact__name">Marcus</span> 0400 555 182</p>
        <p class="contact__email">marcus@risepasthorizon.com.au</p>
        <p class="contact__role">Manager</p>
      </div>
      <div class="contact">
        <p class="contact__line"><span class="contact__name">Reuben</span> 0400 555 274</p>
        <p class="contact__email">reuben@risepasthorizon.com.au</p>
        <p class="contact__role">Weight Loss Coach</p>
      </div>
      <p class="site">www.risepasthorizon.com.au</p>
      <p class="address">14 Wattle Grove, Kelmscott QLD 4150</p>
    </div>
  </section>

</div>
</body>
</html>
```